LABEL DESIGNS FOR SKINCARE LINE

Hello we are needing 12 label various label designs but would like to see you design ONE. We will pick winner from this and send the rest.
LABEL SIZE -2x7
JAR SIZE IS - 8oz
LOGOS FILES BELOW
https://vault.parcelnook.net/share/folders/7Kp3wQ-zrTbnvLoYcDFeMJHAXUw9PsR2a
INFORMATION FOR LABEL
Lumi Dawn Halo Whipped Body Sugar Scrub 8oz
Ideal for all Skin Types
Ingredients:
Pure Cane Sugar, Extra Virgin Coconut Oil, Mango Butter, Kukum Butter, Emulsifying Wax, Jojoba Seed Oil, Sweet Almond Oil, Strawberry Essential Oil, and Pomegranate Essential Oil.
Directions to use Body Sugar Scrub:
Apply to wet skin gently in a circular motion on desired body area, hands, feet, legs, arms, etc. Once you have a good scrub, rinse, pat dry, and enjoy soft, hydrated skin. Best to use in the shower. Use between 2-3 times a week if needed.
*Cautions:
(1) Allergy: Approach this product with extreme caution, if you have allergies
(2) Avoid direct contact with eyes
Storage/Shelf Life of Product:
For best results, stir/mix scrub with the wooden or plastic spoon before each use. The shelf life of all sugar scrubs is 6-8 weeks. Keep the product in a cool, dry place, away from hot or heated temperatures.
All Natural, Cruelty-Free, Vegan Free
No Mineral Oil
No Petroleum
No Parabens

```html
<!DOCTYPE html>
<html lang="en">
<head>
<meta charset="utf-8">
<title>Lumi Dawn Halo Whipped Body Sugar Scrub Labels</title>
<link href="https://fonts.googleapis.com/css2?family=Oswald:wght@400;600&family=Playfair+Display:wght@600&family=Pacifico&family=Dancing+Script:wght@700&display=swap" rel="stylesheet">
<style>
  :root {
    --page: #ffffff;
    --red-deep: #c8101c;
    --red-mid: #e5212d;
    --red-light: #f0525a;
    --pink-deep: #e0174f;
    --pink-mid: #ef3f7a;
    --pink-light: #f66fa0;
    --ink: #ffffff;
  }
  html, body {
    margin: 0;
    padding: 0;
    width: 864px;
    height: 1200px;
    overflow: hidden;
    background: var(--page);
  }
  .canvas {
    position: relative;
    width: 864px;
    height: 1200px;
  }
  .label {
    position: absolute;
    left: 86px;
    width: 694px;
    height: 198px;
    overflow: hidden;
    color: var(--ink);
    font-family: "Oswald", sans-serif;
    font-weight: 400;
  }
  .label--red { top: 380px; }
  .label--pink { top: 658px; }
  .label__backdrop {
    position: absolute;
    inset: 0;
  }
  .label--red .label__backdrop {
    background:
      radial-gradient(ellipse at 70% 40%, var(--red-light) 0%, transparent 55%),
      linear-gradient(180deg, var(--red-mid) 0%, var(--red-deep) 100%);
  }
  .label--pink .label__backdrop {
    background:
      linear-gradient(120deg, transparent 40%, rgba(255,255,255,0.12) 40%, rgba(255,255,255,0.12) 60%, transparent 60%),
      linear-gradient(100deg, var(--pink-mid) 0%, var(--pink-deep) 45%, var(--pink-light) 75%, var(--pink-deep) 100%);
  }
  .panel {
    position: absolute;
    top: 22px;
    width: 182px;
    font-size: 10.2px;
    line-height: 13.3px;
  }
  .panel--left { left: 29px; }
  .panel--right { left: 484px; }
  .panel p { margin: 0 0 12px; }
  .panel strong { font-weight: 600; }
  .claims {
    text-align: center;
    font-weight: 600;
    margin-top: 14px !important;
  }
  .center {
    position: absolute;
    left: 250px;
    width: 194px;
    top: 14px;
    text-align: center;
  }
  .brand {
    display: inline-flex;
    align-items: center;
    gap: 4px;
    font-family: "Oswald", sans-serif;
    font-weight: 600;
    font-size: 15px;
    line-height: 20px;
  }
  .brand__dot {
    width: 5px;
    height: 5px;
    border-radius: 50%;
    background: var(--ink);
  }
  .product-sub {
    font-family: "Dancing Script", cursive;
    font-size: 23px;
    line-height: 24px;
    margin-top: 6px;
  }
  .product-main {
    font-size: 50px;
    line-height: 52px;
  }
  .label--red .product-main { font-family: "Playfair Display", serif; font-weight: 600; }
  .label--pink .product-main { font-family: "Pacifico", cursive; font-size: 42px; line-height: 54px; }
  .product-type {
    font-weight: 600;
    font-size: 15px;
    line-height: 20px;
    margin-top: 2px;
  }
  .size {
    font-weight: 600;
    font-size: 14px;
    line-height: 20px;
    margin-top: 4px;
  }
</style>
</head>
<body>
<main class="canvas">

  <section class="label label--red">
    <div class="label__backdrop" role="img" aria-label="Red sparkling glitter background"></div>
    <div class="panel panel--left">
      <p><strong>Ingredients:</strong> Pure Cane Sugar, Extra Virgin Coconut Oil, Mango Butter, Kukum Butter, Emulsifying Wax, Jojoba Seed Oil, Sweet Almond Oil, Strawberry Essential Oil, and Pomegranate Essential Oil.</p>
      <p><strong>Storage/Shelf Life of Product:</strong> For best results, stir/mix scrub with the wooden or plastic spoon before each use. The shelf life of all sugar scrubs is 6-8 weeks. Keep the product in a cool, dry place, away from hot or heated temperatures.</p>
    </div>
    <div class="center">
      <div class="brand"><span class="brand__dot"></span>Honey Glow Co.</div>
      <div class="product-sub">Lumi Dawn</div>
      <div class="product-main">Halo</div>
      <div class="product-type">Whipped Body Sugar Scrub</div>
      <div class="size">8oz</div>
    </div>
    <div class="panel panel--right">
      <p><strong>Directions:</strong> Apply to wet skin gently in a circular motion on desired body area, hands, feet, legs, arms, etc. Once you have a good scrub, rinse, pat dry, and enjoy soft, hydrated skin. Best to use in the shower. Use between 2-3 times a week if needed.</p>
      <p><strong>Cautions:</strong> (1) Allergy: Approach this product with extreme caution, if you have allergies (2) Avoid direct contact with eyes</p>
      <p class="claims">All Natural, Cruelty-Free, Vegan Free<br>No Mineral Oil | No Petroleum | No Parabens</p>
    </div>
  </section>

  <section class="label label--pink">
    <div class="label__backdrop" role="img" aria-label="Pink background with soft light bands and faint sparkles"></div>
    <div class="panel panel--left">
      <p><strong>Ingredients:</strong> Pure Cane Sugar, Extra Virgin Coconut Oil, Mango Butter, Kukum Butter, Emulsifying Wax, Jojoba Seed Oil, Sweet Almond Oil, Strawberry Essential Oil, and Pomegranate Essential Oil.</p>
      <p><strong>Storage/Shelf Life of Product:</strong> For best results, stir/mix scrub with the wooden or plastic spoon before each use. The shelf life of all sugar scrubs is 6-8 weeks. Keep the product in a cool, dry place, away from hot or heated temperatures.</p>
    </div>
    <div class="center">
      <div class="brand"><span class="brand__dot"></span>Honey Glow Co.</div>
      <div class="product-sub">Lumi Dawn</div>
      <div class="product-main">Halo</div>
      <div class="product-type">Whipped Body Sugar Scrub</div>
      <div class="size">8oz</div>
    </div>
    <div class="panel panel--right">
      <p><strong>Directions:</strong> Apply to wet skin gently in a circular motion on desired body area, hands, feet, legs, arms, etc. Once you have a good scrub, rinse, pat dry, and enjoy soft, hydrated skin. Best to use in the shower. Use between 2-3 times a week if needed.</p>
      <p><strong>Cautions:</strong> (1) Allergy: Approach this product with extreme caution, if you have allergies (2) Avoid direct contact with eyes</p>
      <p class="claims">All Natural, Cruelty-Free, Vegan Free<br>No Mineral Oil | No Petroleum | No Parabens</p>
    </div>
  </section>

</main>
</body>
</html>
```